Business Card Design Project

We need a Business Card for an Mechanical Engineering firm in Singapore. The design should be Modern & Technical looking, yet eye catching.

Our company deals in Cutting Tools & Machine Accessories for the Manufacturing Industries such as Oil & Gas, Aero Space, etc... For more information on our Company, you can either email me or view our website www.valtrion.com.sg.

We are trying to revamp our image to give our consumers a fresh new perspective to our company, so we welcome all ideas.

Industry/Entity Type

Business

Requirements
Must have
• Must incorporate New Company Logo into the card as shown in Uploaded file.

```html
<!DOCTYPE html>
<html lang="en">
<head>
<meta charset="utf-8">
<title>Valtrion Tools – Business Card</title>
<link rel="stylesheet" href="https://fonts.googleapis.com/css2?family=Lato:wght@400;700&display=swap">
<style>
  :root {
    --crimson: #a3123f;
    --crimson-dark: #8c0f36;
    --ink: #2b2b2b;
    --paper: #ffffff;
    --backdrop: #e6eaec;
    --on-crimson: #ffffff;
  }
  * { box-sizing: border-box; margin: 0; padding: 0; }
  html, body { width: 1200px; height: 960px; overflow: hidden; }
  body {
    background: var(--backdrop);
    font-family: "Lato", sans-serif;
    position: relative;
  }
  .card {
    position: absolute;
    left: 320px;
    width: 560px;
    height: 320px;
    background: var(--paper);
    overflow: hidden;
    box-shadow: 0 6px 18px rgba(0,0,0,.18);
  }
  .card--front { top: 90px; }
  .card--back { top: 530px; }

  /* Wordmark */
  .wordmark {
    position: absolute;
    display: flex;
    align-items: center;
    gap: 12px;
    color: var(--ink);
    font-weight: 400;
    font-size: 34px;
    letter-spacing: 1px;
    text-transform: uppercase;
    white-space: nowrap;
  }
  .wordmark__dot {
    width: 34px; height: 34px;
    border-radius: 50%;
    background: var(--crimson);
  }
  .card--front .wordmark { left: 50%; top: 62px; transform: translateX(-50%); }
  .card--back .wordmark { left: 50%; top: 50%; transform: translate(-50%, -50%); }

  /* Front card */
  .front__rule {
    position: absolute; left: 0; right: 0; top: 168px;
    height: 4px; background: var(--crimson);
  }
  .front__band {
    position: absolute; left: 0; right: 0; top: 180px; bottom: 0;
    background: var(--crimson);
    color: var(--on-crimson);
  }
  .person { position: absolute; left: 30px; top: 36px; }
  .person__name { font-size: 29px; font-weight: 400; line-height: 1.15; }
  .person__title { font-size: 18px; font-weight: 400; margin-top: 4px; }
  .contact {
    position: absolute; left: 318px; top: 14px;
    font-size: 12.5px; line-height: 1.45;
  }
  .contact__list { list-style: none; }
  .contact__item { display: flex; align-items: center; gap: 9px; height: 19px; }
  .contact__item svg { width: 11px; height: 11px; flex: none; }
  .contact__item--web { font-weight: 700; }
  .contact__address { margin-top: 8px; padding-left: 0; font-style: normal; }

  /* Back card */
  .back__band { position: absolute; left: 0; right: 0; background: var(--crimson); }
  .back__band--top { top: 0; height: 34px; }
  .back__band--bottom { bottom: 0; height: 66px; }
</style>
</head>
<body>

  <section class="card card--front" aria-label="Business card front">
    <div class="wordmark"><span>Valtrion Tools</span><span class="wordmark__dot"></span></div>
    <div class="front__rule"></div>
    <div class="front__band">
      <div class="person">
        <p class="person__name">Arjun Mehta</p>
        <p class="person__title">Operations Director</p>
      </div>
      <div class="contact">
        <ul class="contact__list">
          <li class="contact__item">
            <svg viewBox="0 0 12 12" aria-hidden="true"><rect x="3" y="0.5" width="6" height="11" rx="1" fill="none" stroke="#fff" stroke-width="1.2"/><rect x="4.3" y="2" width="3.4" height="5" fill="#fff"/></svg>
            <span>65-61234567</span>
          </li>
          <li class="contact__item">
            <svg viewBox="0 0 12 12" aria-hidden="true"><rect x="0.6" y="2.2" width="10.8" height="7.6" fill="none" stroke="#fff" stroke-width="1.2"/><path d="M0.6 2.2 6 6.8 11.4 2.2" fill="none" stroke="#fff" stroke-width="1.2"/></svg>
            <span>hello@valtrion.com.sg</span>
          </li>
          <li class="contact__item contact__item--web">
            <svg viewBox="0 0 12 12" aria-hidden="true"><circle cx="6" cy="6" r="5.3" fill="none" stroke="#fff" stroke-width="1.2"/><ellipse cx="6" cy="6" rx="2.2" ry="5.3" fill="none" stroke="#fff" stroke-width="1"/><path d="M0.7 6h10.6" stroke="#fff" stroke-width="1"/></svg>
            <span>www.valtrion.com.sg</span>
          </li>
        </ul>
        <address class="contact__address">27 Kallang Way #02-15,<br>Meridian Industrial Park,<br>Singapore 349321</address>
      </div>
    </div>
  </section>

  <section class="card card--back" aria-label="Business card back">
    <div class="back__band back__band--top"></div>
    <div class="wordmark"><span>Valtrion Tools</span><span class="wordmark__dot"></span></div>
    <div class="back__band back__band--bottom"></div>
  </section>

</body>
</html>
```